Aviation security consulting company needs a website

We need a website design for Brisk Holloway, and aviation security consulting company. Brisk Holloway (www.briskholloway.example) is an aviation security consulting company that works with government and industry stakeholders in over 60 countries on aviation security strategy, governance, and oversight at the regulatory and operational level.
Brisk Holloway is strongly internationally focused.
The website required should be simple, corporate, serious, and communicate professionalism, reliability and honesty. We are trying to give the company a feeling of being well established.
The attached files include the company logo, along with examples of company web page styles that we like.
The Brisk Holloway website need only be around five pages long (landing page, who we are, our services, our clients, contact), though don't feel limited to only five pages.
The existing website (www.briskholloway.example) was rushed and put together using Wix. We don't love the existing website as it looks too amateur, so don't use it as a template.
There is no requirement for any online sales tools to be included in the site. The site is purely informational, with the option of people making contact via email.

```html
<!DOCTYPE html>
<html lang="en">
<head>
<meta charset="utf-8">
<title>Brisk Holloway — Aviation Security Consulting</title>
<link href="https://fonts.googleapis.com/css2?family=Open+Sans:wght@300;400;600;700&display=swap" rel="stylesheet">
<style>
:root{
  --navy:#1c2b63;
  --navy-deep:#14203f;
  --footer:#1a2540;
  --ink:#2b2f3a;
  --muted:#666b75;
  --heading:#1f2e66;
  --white:#ffffff;
  --soft:#f2f2f2;
  --line:#1f2e66;
}
*{margin:0;padding:0;box-sizing:border-box}
html,body{width:1200px;height:3529px;overflow:hidden}
body{position:relative;font-family:"Open Sans",sans-serif;color:var(--ink);background:var(--white)}
.abs{position:absolute}
.photo{position:absolute}

/* hero */
.hero{position:absolute;left:0;top:0;width:1200px;height:558px;overflow:hidden}
.hero-photo{inset:0;background:linear-gradient(180deg,#3f5f8f 0%,#7f9bbd 35%,#a8b6c4 62%,#5a6575 78%,#2f3540 100%)}
.brand{left:155px;top:20px;display:flex;align-items:center;gap:8px;color:var(--white)}
.brand-mark{width:44px;height:44px;border:3px solid var(--white)}
.brand-name{font-size:27px;font-weight:700;line-height:1}
.brand-tag{font-size:10px;letter-spacing:1px;display:block;margin-top:2px;font-weight:400}
.nav{right:190px;top:30px;display:flex;gap:36px}
.nav a{color:var(--white);text-decoration:none;font-size:13px;font-weight:600;position:relative;padding-bottom:14px}
.nav a.active::after{content:"";position:absolute;left:0;right:0;bottom:0;height:2px;background:var(--white)}
.frame{position:absolute;width:56px;height:56px;border-color:var(--white);border-style:solid;border-width:0}
.tl{border-top-width:2px;border-left-width:2px}
.tr{border-top-width:2px;border-right-width:2px}
.bl{border-bottom-width:2px;border-left-width:2px}
.br{border-bottom-width:2px;border-right-width:2px}
.hero-title{left:0;width:1200px;top:254px;text-align:center;color:var(--white);font-size:33px;font-weight:400;letter-spacing:3px}
.hero-sub{left:0;width:1200px;top:296px;text-align:center;color:#eef2f7;font-size:17px;font-weight:300}
.btn-outline{display:block;border:1.5px solid var(--white);color:var(--white);font-size:12px;text-align:center;text-decoration:none}

/* section headings */
.section-title{font-size:25px;font-weight:400;color:var(--heading)}
.section-title::after{content:"";display:block;width:100px;height:2px;background:currentColor;margin-top:8px}
.on-dark{color:var(--white)}

/* about */
.vline{position:absolute;width:3px;background:var(--line)}
.about-text{left:687px;top:812px;width:355px;font-size:11.5px;line-height:1.6;color:var(--muted)}
.about-text p+p{margin-top:14px}

/* services */
.services{position:absolute;left:0;top:1127px;width:1200px;height:845px;background:var(--navy)}
.card{position:absolute;width:280px;height:296px;background:var(--white)}
.card-photo{position:absolute;left:0;top:0;width:280px;height:137px}
.card-title{position:absolute;left:22px;top:156px;font-size:14px;font-weight:700;color:var(--heading)}
.card-text{position:absolute;left:22px;top:180px;width:240px;font-size:11px;line-height:1.55;color:var(--muted)}

/* review */
.review-text{left:155px;top:2207px;width:352px;font-size:11.5px;line-height:1.6;color:var(--muted)}
.review-name{left:155px;top:2320px;font-size:17px;color:var(--heading)}
.review-role{left:155px;top:2346px;font-size:11px;color:var(--muted)}
.arrow-dot{position:absolute;width:24px;height:24px;border-radius:50%;background:#7a8088}

/* clients */
.clients{position:absolute;left:0;top:2548px;width:1200px;height:264px;background:var(--soft)}
.client{position:absolute;display:flex;align-items:center;gap:8px;font-size:22px;font-weight:700;color:var(--navy)}
.client-dot{width:22px;height:22px;background:var(--navy)}
.badge{position:absolute;border-radius:50%}

/* contact */
.contact{position:absolute;left:0;top:2812px;width:1200px;height:637px}
.contact-photo{inset:0;background:linear-gradient(180deg,#0f1e3d 0%,#1a2e55 45%,#3c4c6a 70%,#1b2846 100%)}
.contact-title{left:0;width:1200px;top:2910px;text-align:center;font-size:31px;letter-spacing:2px;color:var(--white);font-weight:400}
.contact-sub{left:0;width:1200px;top:2954px;text-align:center;font-size:13px;line-height:1.45;color:var(--white)}
.field{position:absolute;left:461px;width:278px;border-bottom:1px solid rgba(255,255,255,.6);font-size:11px;font-style:italic;color:#c8cfdb;text-align:center;padding-bottom:8px}
.send{position:absolute;left:541px;top:3308px;width:120px;height:30px;background:#9aa3b4;color:var(--white);font-size:12px;display:flex;align-items:center;justify-content:center;gap:8px}

/* footer */
.footer{position:absolute;left:0;top:3449px;width:1200px;height:80px;background:var(--footer)}
.copyright{position:absolute;left:155px;top:31px;font-size:14px;color:#9aa3b4}
.to-top{position:absolute;left:1026px;top:30px}
</style>
</head>
<body>

<header class="hero">
  <div class="photo hero-photo" role="img" aria-label="Business jets parked on an airport apron under a blue sky"></div>
  <div class="abs brand">
    <span class="brand-mark"></span>
    <span><span class="brand-name">Brisk Holloway</span><span class="brand-tag">aviation security consulting</span></span>
  </div>
  <nav class="abs nav">
    <a class="active" href="#">Home</a><a href="#">About</a><a href="#">Services</a><a href="#">Clients</a><a href="#">Contact</a>
  </nav>
  <span class="frame tl" style="left:308px;top:221px"></span>
  <span class="frame tr" style="left:836px;top:221px"></span>
  <span class="frame bl" style="left:308px;top:363px"></span>
  <span class="frame br" style="left:836px;top:363px"></span>
  <h1 class="abs hero-title">Aviation Security Consulting</h1>
  <p class="abs hero-sub">with experience in over 60 countries</p>
  <a class="abs btn-outline" href="#" style="left:536px;top:343px;width:128px;line-height:29px">Consult Now</a>
</header>

<section class="about">
  <span class="vline" style="left:335px;top:593px;height:94px"></span>
  <div class="photo" style="left:155px;top:663px;width:280px;height:361px;background:linear-gradient(135deg,#d9dde3,#eef0f2 50%,#9aa0a8)" role="img" aria-label="Business team reviewing documents at an office desk"></div>
  <div class="photo" style="left:383px;top:743px;width:205px;height:201px;background:linear-gradient(180deg,#2f6fb5,#7fb0de)" role="img" aria-label="Passenger jet climbing into a blue sky"></div>
  <span class="vline" style="left:255px;top:1024px;height:70px"></span>
  <h2 class="abs section-title" style="left:687px;top:742px">About Us</h2>
  <div class="abs about-text">
    <p>Brisk Holloway is a full service aviation security consulting company with experience in over 60 countries. We work with government and industry stakeholders to deliver outstanding security outcomes at both a regulatory and operational level.</p>
    <p>Contact us to discuss your aviation security requirements and how we can work in partnership to ensure you exceed your domestic and international aviation security obligations.</p>
  </div>
</section>

<section class="services">
  <h2 class="abs section-title on-dark" style="left:155px;top:40px">Our Services</h2>

  <article class="card" style="left:155px;top:115px">
    <div class="card-photo" style="background:linear-gradient(135deg,#2a2c33,#6d6f76)" role="img" aria-label="Flight crew in uniform beside an aircraft"></div>
    <h3 class="card-title">Civil Aviation Authority</h3>
    <p class="card-text">Aviation security regulatory agencies are required to navigate a plethora of conflicting domestic regulation, along with regional and international aviation security requirements.</p>
  </article>
  <article class="card" style="left:459px;top:115px">
    <div class="card-photo" style="background:linear-gradient(180deg,#3a3f4f,#a08a66)" role="img" aria-label="Busy airport terminal hall"></div>
    <h3 class="card-title">Airport Operations</h3>
    <p class="card-text">Brisk Holloway can work with airports and airport designers to ensure security is incorporated in airport designs, and is maximised within existing airport environments.</p>
  </article>
  <article class="card" style="left:765px;top:115px">
    <div class="card-photo" style="background:linear-gradient(180deg,#8fb3d6,#c9c9c4 60%,#b23a2e)" role="img" aria-label="Cargo containers being loaded onto an aircraft"></div>
    <h3 class="card-title">Air Cargo / Handling Agent</h3>
    <p class="card-text">Air cargo security is seeing rapid changes, with issues such as pre-loading advanced cargo information, electronic consignment security declarations, and secure supply chains becoming more important.</p>
  </article>

  <article class="card" style="left:155px;top:438px">
    <div class="card-photo" style="background:linear-gradient(180deg,#b9c2cc,#5e6672)" role="img" aria-label="Passengers at airport check-in counters"></div>
    <h3 class="card-title">Capacity Development</h3>
    <p class="card-text">Brisk Holloway has extensive experience working in partnership with developing economies to implement incremental changes to aviation security that don't just meet immediate needs.</p>
  </article>
  <article class="card" style="left:459px;top:438px">
    <div class="card-photo" style="background:linear-gradient(135deg,#1d2a3a,#3e5d7a)" role="img" aria-label="Operator at an airline operations control desk"></div>
    <h3 class="card-title">Airline</h3>
    <p class="card-text">Brisk Holloway can work with airlines on security issues such as security program development, station inspection and audit, strategic guidance, and change management.</p>
  </article>
  <article class="card" style="left:765px;top:438px">
    <div class="card-photo" style="background:linear-gradient(180deg,#9ab0c6,#2c3440)" role="img" aria-label="Pilots at the controls in an aircraft cockpit"></div>
    <h3 class="card-title">Training</h3>
    <p class="card-text">Brisk Holloway has experienced aviation security trainers who can take participants through course material prepared by your organisation, or can develop training material tailored to your requirements.</p>
  </article>

  <a class="abs btn-outline" href="#" style="left:536px;top:762px;width:128px;line-height:31px">Explore More</a>
</section>

<section class="review">
  <h2 class="abs section-title" style="left:155px;top:2144px">Client Review</h2>
  <p class="abs review-text">Lorem Ipsum has been the industry's standard dummy text ever since the 1500s, when an unknown printer took a galley of type and scrambled it to make a type specimen book. It has survived not only five centuries, but also the leap into electronic typesetting, remaining essentially unchanged.</p>
  <p class="abs review-name">Dorian Pelletier</p>
  <p class="abs review-role">CEO, Company Name</p>

  <span class="vline" style="left:865px;top:2005px;height:96px"></span>
  <div class="photo" style="left:765px;top:2075px;width:280px;height:360px;background:linear-gradient(180deg,#d9c9a8,#b9b2a6 45%,#6b7077 75%,#3a3c40)" role="img" aria-label="Wide-body airliner parked on the apron at dusk"></div>
  <div class="photo" style="left:612px;top:2155px;width:204px;height:205px;background:linear-gradient(135deg,#3f7fb8,#a9c8e2 60%,#2a2f3a)" role="img" aria-label="Portrait of the reviewing client in a suit"></div>
  <span class="vline" style="left:940px;top:2435px;height:71px"></span>
  <span class="arrow-dot" style="left:612px;top:2362px"></span>
  <span class="arrow-dot" style="left:640px;top:2362px"></span>
  <svg class="abs" style="left:612px;top:2362px" width="52" height="24" viewBox="0 0 52 24" aria-hidden="true">
    <path d="M14 7 L9 12 L14 17" fill="none" stroke="#fff" stroke-width="2"/>
    <path d="M38 7 L43 12 L38 17" fill="none" stroke="#fff" stroke-width="2"/>
  </svg>
</section>

<section class="clients">
  <h2 class="abs section-title" style="left:155px;top:38px">Our Clients</h2>
  <div class="client" style="left:155px;top:138px"><span class="client-dot"></span>Vantor Risk</div>
  <span class="badge" style="left:393px;top:118px;width:66px;height:66px;background:#c4262e"></span>
  <div class="client" style="left:534px;top:138px">Keelstone</div>
  <span class="badge" style="left:718px;top:118px;width:66px;height:66px;background:#3a4d7a"></span>
  <div class="client" style="left:866px;top:138px"><span class="client-dot"></span>Aerolink Agent</div>
</section>

<section class="contact">
  <div class="photo contact-photo" role="img" aria-label="Airliner engine and wing at night on the tarmac"></div>
</section>
<span class="frame tl" style="left:308px;top:2873px"></span>
<span class="frame tr" style="left:836px;top:2873px"></span>
<span class="frame bl" style="left:308px;top:3325px"></span>
<span class="frame br" style="left:836px;top:3325px"></span>
<h2 class="abs contact-title">Contact Us</h2>
<p class="abs contact-sub">Whatever your aviation security requirements, contact us to discuss<br>solutions appropriate to your operating environment</p>
<div class="field" style="top:3022px">Your Name</div>
<div class="field" style="top:3075px">Enter Your Email</div>
<div class="field" style="top:3132px">Subject</div>
<div class="field" style="top:3184px;height:92px">Type Message</div>
<div class="send">
  <svg width="14" height="12" viewBox="0 0 14 12" aria-hidden="true"><path d="M0 5 L14 0 L10 12 L7 7 Z" fill="#fff"/></svg>
  Send
</div>

<footer class="footer">
  <p class="copyright">© 2016 Brisk Holloway</p>
  <svg class="to-top" width="18" height="20" viewBox="0 0 18 20" aria-label="Back to top">
    <path d="M9 2 L2 9 M9 2 L16 9 M9 2 V18" fill="none" stroke="#ffffff" stroke-width="3"/>
  </svg>
</footer>

</body>
</html>
```